Digital Transformation Company Trade Show Banners

I am looking for help designing banners for an upcoming trade show. One would be for our company and one would be for our product. I am planning on purchasing retractable banners with a size of 33" x 81". Details are attached.

```html
<!DOCTYPE html>
<html lang="en">
<head>
<meta charset="UTF-8">
<title>Voltara Systems – Trade Show Banner</title>
<link href="https://fonts.googleapis.com/css2?family=Poppins:wght@500;600;700;800&display=swap" rel="stylesheet">
<style>
  :root {
    --orange: #ee7a30;
    --orange-footer: #ec8a45;
    --blue: #4f8bc0;
    --ink: #111111;
    --dark: #050505;
    --paper: #ffffff;
    --mist: #eef3f8;
    --stage: #ececec;
  }
  * { margin: 0; padding: 0; box-sizing: border-box; }
  html, body { width: 1200px; height: 2873px; overflow: hidden; }
  body {
    background: var(--stage);
    font-family: "Poppins", sans-serif;
    position: relative;
  }
  .banner {
    position: absolute;
    left: 15px; top: 0;
    width: 1170px; height: 2873px;
    background: var(--paper);
    overflow: hidden;
  }
  .header {
    position: absolute; left: 0; top: 0; width: 100%; height: 355px;
    background: linear-gradient(180deg, #fafbfc 0%, #f1f4f7 100%);
  }
  .brand {
    position: absolute; left: 0; right: 0; top: 120px;
    display: flex; align-items: center; justify-content: center; gap: 26px;
  }
  .brand-mark { width: 44px; height: 44px; background: var(--orange); }
  .brand-name {
    font-weight: 700; font-size: 76px; letter-spacing: 4px; color: var(--ink); line-height: 1;
  }
  .hero-art { position: absolute; left: 0; top: 0; width: 100%; height: 1300px; }
  .hero-copy {
    position: absolute; left: 120px; top: 520px;
    color: var(--paper); font-weight: 600; line-height: 1.12; font-size: 126px;
    letter-spacing: -1px;
  }
  .hero-copy .accent { color: var(--orange); font-weight: 800; }
  .hero-copy .small { font-size: 88px; }
  .services {
    position: absolute; left: 0; top: 1300px; width: 100%; height: 1343px;
    background: linear-gradient(160deg, #ffffff 0%, var(--mist) 55%, #f7f9fb 100%);
  }
  .offer-title {
    position: absolute; left: 126px; top: 70px;
    display: flex; align-items: baseline; gap: 50px;
  }
  .offer-title .lead { font-weight: 800; font-size: 88px; color: var(--ink); letter-spacing: 1px; }
  .offer-title .tail { font-weight: 700; font-size: 48px; color: var(--ink); }
  .offer-sub {
    position: absolute; left: 126px; top: 190px;
    font-weight: 600; font-size: 80px; color: var(--orange); line-height: 1;
  }
  .service {
    position: absolute; left: 126px; width: 960px;
    display: flex; align-items: center; gap: 100px;
  }
  .service svg { width: 140px; height: 140px; flex: none; }
  .service-name {
    font-weight: 700; font-size: 50px; color: var(--ink); line-height: 1.15; text-transform: uppercase;
  }
  .footer {
    position: absolute; left: 0; bottom: 0; width: 100%; height: 230px;
    background: var(--orange-footer);
  }
  .footer-ask {
    position: absolute; left: 126px; top: 74px;
    font-weight: 700; font-size: 46px; line-height: 1.15; color: var(--ink);
  }
  .footer-ask .light { color: var(--paper); }
  .footer-arrow { position: absolute; left: 350px; top: -18px; width: 180px; height: 60px; }
  .contact { position: absolute; left: 466px; top: 62px; color: var(--paper); }
  .contact-row { display: flex; align-items: center; gap: 34px; }
  .contact-row svg { width: 56px; height: 56px; flex: none; }
  .phone { font-weight: 700; font-size: 74px; line-height: 1; }
  .web { font-weight: 500; font-size: 52px; line-height: 1; margin-top: 14px; }
</style>
</head>
<body>
<div class="banner">
  <header class="header">
    <div class="brand">
      <span class="brand-mark"></span>
      <span class="brand-name">VOLTARA SYSTEMS</span>
    </div>
  </header>

  <svg class="hero-art" viewBox="0 0 1170 1300" preserveAspectRatio="none">
    <rect x="0" y="355" width="1170" height="945" fill="var(--dark)"/>
    <defs>
      <linearGradient id="photoTone" x1="0" y1="0" x2="1" y2="1">
        <stop offset="0" stop-color="#3a2a22"/>
        <stop offset="0.5" stop-color="#24201e"/>
        <stop offset="1" stop-color="#1a1c22"/>
      </linearGradient>
    </defs>
    <rect x="112" y="475" width="900" height="700" fill="url(#photoTone)" role="img" aria-label="Photo of a person working at a laptop in a modern office"/>
    <polygon points="1170,271 1170,1300 405,1300" fill="var(--blue)" opacity="0.93"/>
  </svg>
  <h1 class="hero-copy">
    LOOKING TO<br>
    <span class="accent">THRIVE</span> <span class="small">IN THE</span><br>
    DIGITAL AGE?
  </h1>

  <section class="services">
    <div class="offer-title"><span class="lead">WE OFFER</span><span class="tail">A WIDE VARIETY OF</span></div>
    <div class="offer-sub">DIGITAL SERVICES</div>

    <div class="service" style="top:308px">
      <svg viewBox="0 0 64 64" fill="none" stroke="var(--orange)" stroke-width="2.5" stroke-linecap="round">
        <circle cx="30" cy="32" r="8"/><circle cx="30" cy="32" r="3"/>
        <path d="M30 20v-3M30 47v-3M18 32h-3M45 32h-3M21 23l-2-2M41 43l-2-2M21 41l-2 2M41 21l-2 2"/>
        <path d="M14 18a22 22 0 0 1 20-10M50 46a22 22 0 0 1-20 10"/>
        <rect x="44" y="6" width="14" height="18" rx="2"/><rect x="6" y="42" width="14" height="14" rx="2"/>
      </svg>
      <div class="service-name">Digital<br>Transformation</div>
    </div>
    <div class="service" style="top:504px">
      <svg viewBox="0 0 64 64" fill="none" stroke="var(--orange)" stroke-width="2.5" stroke-linecap="round">
        <circle cx="32" cy="32" r="16"/>
        <rect x="25" y="31" width="14" height="11" rx="2"/><path d="M28 31v-4a4 4 0 0 1 8 0v4"/>
        <path d="M32 16V6M32 48v10M16 32H6M48 32h10M21 21l-7-7M43 43l7 7M21 43l-7 7M43 21l7-7"/>
        <circle cx="32" cy="5" r="2"/><circle cx="5" cy="32" r="2"/><circle cx="59" cy="32" r="2"/><circle cx="32" cy="59" r="2"/>
      </svg>
      <div class="service-name">Cybersecurity</div>
    </div>
    <div class="service" style="top:700px">
      <svg viewBox="0 0 64 64" fill="none" stroke="var(--orange)" stroke-width="2.5" stroke-linecap="round">
        <rect x="6" y="8" width="52" height="36" rx="2"/><path d="M6 38h52M26 44v8M38 44v8M20 56h24"/>
        <circle cx="32" cy="24" r="5"/><path d="M14 16h8M42 16h8M14 30h6M44 30h6"/>
      </svg>
      <div class="service-name">Software<br>Development</div>
    </div>
    <div class="service" style="top:910px">
      <svg viewBox="0 0 64 64" fill="none" stroke="var(--orange)" stroke-width="2.5" stroke-linecap="round">
        <path d="M24 38a12 12 0 1 1 16 0v6H24z"/><path d="M26 50h12M28 55h8"/>
        <path d="M32 10V4M14 28H6M58 28h-8M18 14l-5-5M46 14l5-5M16 42l-6 6M48 42l6 6"/>
        <path d="M29 36v-8l3 3 3-3v8"/>
      </svg>
      <div class="service-name">Technology<br>&nbsp;Solution</div>
    </div>
    <div class="service" style="top:1077px">
      <svg viewBox="0 0 64 64" fill="none" stroke="var(--orange)" stroke-width="2.5" stroke-linecap="round">
        <rect x="8" y="6" width="40" height="28" rx="2"/><path d="M14 28l8-10 7 6 12-12"/>
        <circle cx="52" cy="22" r="5"/><path d="M48 34v-4h8v4"/>
        <circle cx="14" cy="44" r="4"/><circle cx="28" cy="44" r="4"/><circle cx="42" cy="44" r="4"/>
        <path d="M8 58v-6h12v6M22 58v-6h12v6M36 58v-6h12v6"/>
      </svg>
      <div class="service-name">Training &amp; Workshops</div>
    </div>
  </section>

  <footer class="footer">
    <svg class="footer-arrow" viewBox="0 0 180 60" fill="none" stroke="var(--ink)" stroke-width="3" stroke-linecap="round">
      <path d="M10 50 Q80 -5 160 40"/><path d="M148 28l12 12-16 4"/>
    </svg>
    <div class="footer-ask"><span class="light">HAVE ANY</span><br>QUESTIONS?</div>
    <div class="contact">
      <div class="contact-row">
        <svg viewBox="0 0 24 24" fill="none" stroke="var(--ink)" stroke-width="1.6" stroke-linejoin="round">
          <path d="M5 3h4l2 5-3 2a11 11 0 0 0 6 6l2-3 5 2v4a2 2 0 0 1-2 2A17 17 0 0 1 3 5a2 2 0 0 1 2-2z"/>
        </svg>
        <span class="phone">(555) 210-4477</span>
      </div>
      <div class="contact-row">
        <svg viewBox="0 0 24 24" fill="none" stroke="var(--ink)" stroke-width="1.6">
          <circle cx="12" cy="12" r="9"/><path d="M3 12h18M12 3c3 3 3 15 0 18M12 3c-3 3-3 15 0 18"/>
        </svg>
        <span class="web">www.voltara.io</span>
      </div>
    </div>
  </footer>
</div>
</body>
</html>
```